Square Business Cards for Our Restaurant / Event Venue

We need square business cards designed for the management team of our event venue and restaurant. On one side of the card should be the the Harbor Lantern 7 logo and URL www.harborlantern7.example. On the other side should be the Ember Logo and URL www.emberhall7.example. All employee details should be on the side with Ember logo. There will be a total of 5 cards to be created with the design.

Clara Bennquist
clara@harborlantern7.example

main 555.418.3072
direct 555.730.2946

4831 West Orchard Lane SE
Washington, DC 90417

Industry/Entity Type

Business

```html
<!DOCTYPE html>
<html lang="en">
<head>
<meta charset="utf-8">
<title>Harbor Lantern 7 — Square Business Cards</title>
<link rel="stylesheet" href="https://fonts.googleapis.com/css2?family=Lato:wght@400;700&display=swap">
<style>
  :root {
    --backdrop: #bdbec0;
    --card: #221f20;
    --card-disc: #2f2d30;
    --brand-red: #b22025;
    --label-red: #a8292b;
    --ink-light: #ffffff;
    --shadow: rgba(0, 0, 0, 0.28);
  }
  * { box-sizing: border-box; margin: 0; padding: 0; }
  html, body {
    width: 1200px;
    height: 685px;
    overflow: hidden;
    background: var(--backdrop);
    font-family: "Lato", Arial, sans-serif;
    color: var(--ink-light);
  }
  .sheet {
    position: relative;
    width: 1200px;
    height: 685px;
  }
  .card {
    position: absolute;
    top: 113px;
    width: 459px;
    height: 459px;
    border-radius: 25px;
    background: var(--card);
    box-shadow: 0 3px 8px var(--shadow);
    overflow: hidden;
  }
  .card--front { left: 113px; }
  .card--back { left: 628px; }

  .line {
    position: absolute;
    left: 0;
    width: 100%;
    text-align: center;
    white-space: nowrap;
  }
  .card-url {
    top: 412px;
    font-size: 16.5px;
    letter-spacing: 1.6px;
  }

  /* Front: venue name lockup */
  .venue-mark {
    position: absolute;
    left: 0;
    top: 229px;
    width: 100%;
    transform: translateY(-50%);
    display: flex;
    align-items: center;
    justify-content: center;
    gap: 14px;
  }
  .venue-mark__dot {
    width: 40px;
    height: 40px;
    border-radius: 50%;
    background: var(--brand-red);
    flex: none;
  }
  .venue-mark__name {
    font-size: 28px;
    font-weight: 400;
    letter-spacing: 0.5px;
    color: var(--ink-light);
  }

  /* Back: contact side */
  .contact-disc {
    position: absolute;
    left: 67px;
    top: 67px;
    width: 324px;
    height: 324px;
    border-radius: 50%;
    background: var(--card-disc);
  }
  .hall-name {
    top: 52px;
    font-size: 42px;
    font-weight: 700;
    letter-spacing: 1px;
  }
  .person-name {
    top: 165px;
    font-size: 17px;
    font-weight: 700;
    letter-spacing: 0.3px;
    text-transform: uppercase;
  }
  .contact-line {
    font-size: 14.5px;
    letter-spacing: 0.3px;
  }
  .contact-line--email { top: 206px; }
  .contact-line--mobile { top: 230px; }
  .contact-line--direct { top: 254px; }
  .contact-line--street { top: 292px; }
  .contact-line--city { top: 316px; }
  .contact-label { color: var(--label-red); }
</style>
</head>
<body>
<main class="sheet">
  <section class="card card--front" aria-label="Card front">
    <div class="venue-mark">
      <span class="venue-mark__dot" aria-hidden="true"></span>
      <span class="venue-mark__name">Harbor Lantern 7</span>
    </div>
    <p class="line card-url">www.harborlantern7.example</p>
  </section>

  <section class="card card--back" aria-label="Card back">
    <div class="contact-disc" aria-hidden="true"></div>
    <p class="line hall-name">Ember</p>
    <p class="line person-name">Clara Bennquist</p>
    <p class="line contact-line contact-line--email">clara@harborlantern7.example</p>
    <p class="line contact-line contact-line--mobile"><span class="contact-label">M:</span> 555.418.3072</p>
    <p class="line contact-line contact-line--direct"><span class="contact-label">D:</span> 555.730.2946</p>
    <p class="line contact-line contact-line--street">4831 West Orchard Lane SE</p>
    <p class="line contact-line contact-line--city">Washington, DC 90417</p>
    <p class="line card-url">www.emberhall7.example</p>
  </section>
</main>
</body>
</html>
```